Brisk Hollow Builders Needs A Flyer

We need a flyer for our newest product "The Cedarlane Garden Workroom"

Here is some copy for the flyer:

1. More and more people everyday are working from home and finding it difficult to disconnect from home activities in order to focus on their work. They are also finding it very expensive to add on to their existing house for a quiet place. Our archatectually stunning, Cedarlane Garden Workroom is the answer. The office studio measures 16' wide and 10' deep. 160 Square feet of space.

Perfect for dozens of purposes. Home office, design studio, artist studio, home school office, reading room, craft studio, drafting room.

Features include:

- Steel Framing. 40-60% lighter then wood, higher strength to weight ratio, resistant to mold and fire and steel is the most recycled material on earth!
- Spray foam insulation. Cool in the summer and warm in the winter.
- HVAC Mini Split with wireless remote control and thermostat.
- 100% Off grid with enough solar and battery storage to run your entire office. No need to pay for an expensive electric installation.
- Flush fitting floor outlets to reduce wires.
- TV mount (Optional with pre-wired electric, HDMI, digital audio & Cat 6)
- Windows are tempered glass custom made by Morvik Glazing.
- Solar qualifies for a 26% tax credit. This is not a write-off rather it is a direct reduction on your tax obligation.
- Thousands of dollars less than adding onto your home.
- Custom color, siding, features available.

This beautiful back yard office is delivered 100% assembled and ready to enjoy on the day of delivery.

We ship nationwide from our factory in South Carolina. Give us a call anytime to speak to a designer and start your dream office today!

555-318-4027
info@BriskHollowBuilders.example

```html
<!DOCTYPE html>
<html lang="en">
<head>
<meta charset="utf-8">
<title>Cedarlane Garden Workroom – Brisk Hollow Builders</title>
<link href="https://fonts.googleapis.com/css2?family=Outfit:wght@600&family=Rubik:wght@400;500;700&display=swap" rel="stylesheet">
<style>
  :root {
    --forest-dark: #12301b;
    --forest: #1f5230;
    --gold: #e9a22f;
    --gold-text: #e7a532;
    --ink: #1d1d1d;
    --panel-grey: #f0f0f2;
    --leaf: #5a9a3a;
    --white: #ffffff;
  }
  * { margin: 0; padding: 0; box-sizing: border-box; }
  html, body { width: 927px; height: 1200px; overflow: hidden; background: var(--white); }
  .flyer { position: relative; width: 927px; height: 1200px; font-family: "Rubik", sans-serif; color: var(--ink); overflow: hidden; }
  .abs { position: absolute; }
  .backdrop { left: 0; top: 0; }
  .intro { left: 36px; top: 15px; width: 851px; color: var(--white); font-size: 15.2px; line-height: 19.8px; text-align: justify; }
  .purposes-title { left: 53px; top: 128px; font-family: "Outfit", sans-serif; font-weight: 600; font-size: 24px; color: var(--white); letter-spacing: -0.2px; }
  .purpose { width: 124px; text-align: center; top: 176px; }
  .purpose-icon { display: block; width: 74px; height: 74px; margin: 0 auto; border: 2px solid var(--white); border-radius: 14px; padding: 8px; }
  .purpose-icon span { display: block; width: 100%; height: 100%; border-radius: 6px; background: rgba(255,255,255,0.18); }
  .purpose-label { margin-top: 15px; color: var(--gold-text); font-weight: 700; font-size: 14.2px; line-height: 18px; white-space: nowrap; }
  .features-title { left: 37px; top: 347px; font-weight: 700; font-size: 18.5px; color: var(--forest); letter-spacing: 0.2px; }
  .feature-list { list-style: none; }
  .feature { position: absolute; left: 27px; width: 533px; padding-left: 46px; font-size: 17.6px; line-height: 22px; text-align: justify; }
  .feature svg { position: absolute; left: 0; top: -1px; }
  .render { border-radius: 2px; }
  .note { left: 600px; width: 327px; color: var(--white); font-size: 15px; line-height: 20px; text-align: justify; }
  .note-green { top: 746px; height: 91px; background: var(--forest); border-top-left-radius: 18px; padding: 9px 27px 0 19px; }
  .note-dark { top: 837px; height: 107px; background: var(--forest-dark); padding: 12px 20px 0 16px; }
  .brand-name { left: 612px; top: 1078px; width: 300px; text-align: center; font-weight: 700; font-size: 22px; color: var(--gold); white-space: nowrap; }
  .phone { left: 612px; top: 1118px; width: 300px; text-align: center; font-weight: 700; font-size: 33px; line-height: 40px; color: var(--leaf); white-space: nowrap; }
  .email { left: 604px; top: 1164px; width: 316px; text-align: center; font-size: 15.4px; color: var(--gold); white-space: nowrap; }
  .photo { top: 1067px; height: 108px; }
</style>
</head>
<body>
<div class="flyer">

  <svg class="abs backdrop" width="927" height="1200" viewBox="0 0 927 1200" aria-hidden="true">
    <rect x="0" y="0" width="927" height="328" fill="var(--forest-dark)"/>
    <path d="M0 155 Q0 117 40 117 L430 117 L474 155 L927 155 L927 328 L0 328 Z" fill="var(--forest)"/>
    <rect x="302" y="160" width="70" height="2.5" fill="var(--gold)"/>
    <path d="M45 203 Q25 203 25 223 L25 290 Q25 306 41 306 L886 306 Q902 306 902 290 L902 223 Q902 203 882 203" fill="none" stroke="var(--gold)" stroke-width="2.5"/>
    <rect x="615" y="328" width="312" height="418" fill="var(--panel-grey)"/>
    <path d="M0 328 L662 328 L615 390 L0 390 Z" fill="var(--gold)"/>
  </svg>

  <p class="abs intro">More and more people everyday are working from home and finding it difficult to disconnect from home activities in order to focus on their work. They are also finding it very expensive to add on to their existing house for a quiet place. Our archatectually stunning, Cedarlane Garden Workroom is the answer. The office studio measures 16' wide and 10' deep. 160 Square feet of space.</p>

  <h2 class="abs purposes-title">Perfect For Dozens Of Purposes</h2>

  <div class="abs purpose" style="left:34px"><span class="purpose-icon" role="img" aria-label="Icon of a person working at a desk"><span></span></span><p class="purpose-label">HOME OFFICE</p></div>
  <div class="abs purpose" style="left:156px"><span class="purpose-icon" role="img" aria-label="Icon of a framed landscape picture"><span></span></span><p class="purpose-label">DESIGN STUDIO</p></div>
  <div class="abs purpose" style="left:279px"><span class="purpose-icon" role="img" aria-label="Icon of an artist with palette and brush"><span></span></span><p class="purpose-label">ARTIST STUDIO</p></div>
  <div class="abs purpose" style="left:401px"><span class="purpose-icon" role="img" aria-label="Icon of a schoolhouse with a student"><span></span></span><p class="purpose-label">HOME SCHOOL<br>OFFICE</p></div>
  <div class="abs purpose" style="left:523px"><span class="purpose-icon" role="img" aria-label="Icon of an open book with a lightbulb"><span></span></span><p class="purpose-label">READING ROOM</p></div>
  <div class="abs purpose" style="left:646px"><span class="purpose-icon" role="img" aria-label="Icon of a hanging do-it-yourself sign"><span></span></span><p class="purpose-label">CRAFT STUDIO</p></div>
  <div class="abs purpose" style="left:768px"><span class="purpose-icon" role="img" aria-label="Icon of a blueprint with a pencil"><span></span></span><p class="purpose-label">DRAFTING ROOM</p></div>

  <h3 class="abs features-title">FEATURES INCLUDE</h3>

  <ul class="feature-list">
    <li class="feature" style="top:422px"><svg width="25" height="25" viewBox="0 0 25 25" aria-hidden="true"><rect x="1.5" y="1.5" width="22" height="22" rx="3" fill="none" stroke="var(--gold)" stroke-width="2.5"/><path d="M7 13 L11 17 L18 8" fill="none" stroke="var(--forest)" stroke-width="2.6" stroke-linecap="round" stroke-linejoin="round"/></svg>Steel Framing. 40-60% lighter then wood, higher strength to weight ratio, resistant to mold and fire and steel is the most recycled material on earth!</li>
    <li class="feature" style="top:510px"><svg width="25" height="25" viewBox="0 0 25 25" aria-hidden="true"><rect x="1.5" y="1.5" width="22" height="22" rx="3" fill="none" stroke="var(--gold)" stroke-width="2.5"/><path d="M7 13 L11 17 L18 8" fill="none" stroke="var(--forest)" stroke-width="2.6" stroke-linecap="round" stroke-linejoin="round"/></svg>Spray foam insulation. Cool in the summer and warm in the winter.</li>
    <li class="feature" style="top:576px"><svg width="25" height="25" viewBox="0 0 25 25" aria-hidden="true"><rect x="1.5" y="1.5" width="22" height="22" rx="3" fill="none" stroke="var(--gold)" stroke-width="2.5"/><path d="M7 13 L11 17 L18 8" fill="none" stroke="var(--forest)" stroke-width="2.6" stroke-linecap="round" stroke-linejoin="round"/></svg>HVAC Mini Split with wireless remote control and thermostat.</li>
    <li class="feature" style="top:642px"><svg width="25" height="25" viewBox="0 0 25 25" aria-hidden="true"><rect x="1.5" y="1.5" width="22" height="22" rx="3" fill="none" stroke="var(--gold)" stroke-width="2.5"/><path d="M7 13 L11 17 L18 8" fill="none" stroke="var(--forest)" stroke-width="2.6" stroke-linecap="round" stroke-linejoin="round"/></svg>100% Off grid with enough solar and battery storage to run your entire office. No need to pay for an expensive electric installation.</li>
    <li class="feature" style="top:730px"><svg width="25" height="25" viewBox="0 0 25 25" aria-hidden="true"><rect x="1.5" y="1.5" width="22" height="22" rx="3" fill="none" stroke="var(--gold)" stroke-width="2.5"/><path d="M7 13 L11 17 L18 8" fill="none" stroke="var(--forest)" stroke-width="2.6" stroke-linecap="round" stroke-linejoin="round"/></svg>Flush fitting floor outlets to reduce wires.</li>
    <li class="feature" style="top:775px"><svg width="25" height="25" viewBox="0 0 25 25" aria-hidden="true"><rect x="1.5" y="1.5" width="22" height="22" rx="3" fill="none" stroke="var(--gold)" stroke-width="2.5"/><path d="M7 13 L11 17 L18 8" fill="none" stroke="var(--forest)" stroke-width="2.6" stroke-linecap="round" stroke-linejoin="round"/></svg>TV mount (Optional with pre-wired electric, HDMI, digital audio &amp; Cat 6)</li>
    <li class="feature" style="top:841px"><svg width="25" height="25" viewBox="0 0 25 25" aria-hidden="true"><rect x="1.5" y="1.5" width="22" height="22" rx="3" fill="none" stroke="var(--gold)" stroke-width="2.5"/><path d="M7 13 L11 17 L18 8" fill="none" stroke="var(--forest)" stroke-width="2.6" stroke-linecap="round" stroke-linejoin="round"/></svg>Windows are tempered glass custom made by Morvik Glazing.</li>
    <li class="feature" style="top:908px"><svg width="25" height="25" viewBox="0 0 25 25" aria-hidden="true"><rect x="1.5" y="1.5" width="22" height="22" rx="3" fill="none" stroke="var(--gold)" stroke-width="2.5"/><path d="M7 13 L11 17 L18 8" fill="none" stroke="var(--forest)" stroke-width="2.6" stroke-linecap="round" stroke-linejoin="round"/></svg>Solar qualifies for a 26% tax credit. This is not a write-off rather it is a direct reduction on your tax obligation.</li>
    <li class="feature" style="top:975px"><svg width="25" height="25" viewBox="0 0 25 25" aria-hidden="true"><rect x="1.5" y="1.5" width="22" height="22" rx="3" fill="none" stroke="var(--gold)" stroke-width="2.5"/><path d="M7 13 L11 17 L18 8" fill="none" stroke="var(--forest)" stroke-width="2.6" stroke-linecap="round" stroke-linejoin="round"/></svg>Thousands of dollars less than adding onto your home.</li>
    <li class="feature" style="top:1019px"><svg width="25" height="25" viewBox="0 0 25 25" aria-hidden="true"><rect x="1.5" y="1.5" width="22" height="22" rx="3" fill="none" stroke="var(--gold)" stroke-width="2.5"/><path d="M7 13 L11 17 L18 8" fill="none" stroke="var(--forest)" stroke-width="2.6" stroke-linecap="round" stroke-linejoin="round"/></svg>Custom color, siding, features available.</li>
  </ul>

  <div class="abs render" role="img" aria-label="Rendering of the garden workroom seen from the front left" style="left:651px;top:352px;width:203px;height:117px;background:linear-gradient(180deg,#3a3a3c 0%,#d9d4cc 35%,#c9c0b3 80%,#3a3a3c 100%)"></div>
  <div class="abs render" role="img" aria-label="Rendering of the garden workroom seen straight on" style="left:725px;top:479px;width:182px;height:105px;background:linear-gradient(180deg,#3a3a3c 0%,#dcd7cf 30%,#cbc2b5 85%,#3a3a3c 100%)"></div>
  <div class="abs render" role="img" aria-label="Rendering of the garden workroom seen from the front right" style="left:640px;top:598px;width:202px;height:115px;background:linear-gradient(180deg,#3a3a3c 0%,#d6d0c7 35%,#c6bdb0 82%,#3a3a3c 100%)"></div>

  <p class="abs note note-green">This beautiful back yard office is delivered 100% assembled and ready to enjoy on the day of delivery.</p>
  <p class="abs note note-dark">We ship nationwide from our factory in South Carolina. Give us a call anytime to speak to a designer and start your dream office today!</p>

  <p class="abs brand-name">Brisk Hollow Builders</p>
  <p class="abs phone">555-318-4027</p>
  <p class="abs email">info@BriskHollowBuilders.example</p>

  <div class="abs photo" role="img" aria-label="Photo of the workroom in a leafy back yard" style="left:0;width:189px;background:linear-gradient(180deg,#7fa6c4 0%,#4d6b3a 40%,#3a3a3a 60%,#54703c 100%)"></div>
  <div class="abs photo" role="img" aria-label="Line drawing of the steel frame structure" style="left:193px;width:189px;background:linear-gradient(180deg,#f4f4f4,#e6e6e6)"></div>
  <div class="abs photo" role="img" aria-label="Photo of the workroom back with solar panels on the roof" style="left:390px;width:190px;background:linear-gradient(180deg,#8fb2cf 0%,#5b7a45 38%,#4a4a4a 60%,#5f7d3f 100%)"></div>

</div>
</body>
</html>
```